Wickedmarlo.com adult webpage with links to various sites she is on.

UPDATE 3/10- let’s keep this a bit more simple. I am uploading three pics and a sketch of how she wants her site to look. It’s really just a page that has her links.

Looking to set up a homepage for my hot wife that has her clickable links on there. Pehaps a space for an about me and some notes encouraging audience to click and join peek vault.
Cashwix link:

https://peekvault.com/away?url=https://Cashwix.com/wickedmarlo

Here is some
Copy from her:
“Queen of Dirty Talk” is important to work in.
🔥HOTWIFE SUPER SLUT🔥

...... I do things the other girls don’t! I suck and fuck like no other woman you’ll ever see. Filthy dirty talk, lots of sloppy oral, fantasy role play, dress up and cum swallowing.

Cum watch me! Have your mind..... and your big fat load blown away!

💋This page is where you will find ALL my links. My free peekvault has my videos for sale. My VIP page you will get the same videos at a discounted prices, plus lots of juicy extras. I also answer all my messages there. Make sure to check out my VIP page today so you don’t miss out on any of the fun!💋💋💋
Updates

I am tryin go to extend the project time to at least two weeks. I just don’t know how to edit. I have an email out to support.

Target Market(s)

Adult entertainment

Industry/Entity Type

Porn

Coding

Coded - Design and coding required

Number of Pages Required

1 page

Colors
000000
eea4c8

Requirements
Must have
• WickedMarlo (no space between) is her stage name.
She would like maybe some cute horns in the logo. Maybe make the “S” have little devil horns on top and roll the bottom of the “S” like a devil tail with the arrows/spade point at at end.
A hot pic of her in background.
Buttons to her various pages.
Nice to have
• Perhaps an about me drop down or window we can write copy for? Pink black and leopard are good color choices.

```html
<!DOCTYPE html>
<html lang="en">
<head>
<meta charset="utf-8">
<title>WickedMarlo</title>
<link href="https://fonts.googleapis.com/css2?family=Figtree:wght@400;500;600;700&display=swap" rel="stylesheet">
<style>
  :root {
    --black: #000000;
    --panel: #121212;
    --pink: #eea4c8;
    --pink-deep: #e480b0;
    --white: #ffffff;
    --text-muted: #b9b9b9;
    --divider: #6b4a5a;
  }
  * { box-sizing: border-box; margin: 0; padding: 0; }
  html, body { width: 919px; height: 1200px; overflow: hidden; background: var(--black); }
  body { font-family: "Figtree", sans-serif; color: var(--white); }
  .page { position: relative; width: 919px; height: 1200px; overflow: hidden;
    background: linear-gradient(180deg, var(--panel) 0, var(--black) 480px); }

  .site-nav { position: absolute; top: 0; left: 0; width: 919px; height: 88px; }
  .site-nav a { position: absolute; top: 33px; font-size: 11px; color: var(--white); text-decoration: none; letter-spacing: .2px; }
  .site-nav a.is-active { color: var(--pink); }
  .site-nav .sep { position: absolute; top: 33px; width: 1px; height: 12px; background: var(--divider); }
  .brand-mark { position: absolute; top: 29px; left: 405px; width: 100px; text-align: center;
    font-size: 15px; font-weight: 600; color: var(--pink); }

  .hero { position: absolute; left: 73px; top: 97px; width: 795px; height: 374px;
    border-radius: 0 65px 0 65px; overflow: hidden;
    background: radial-gradient(ellipse at 45% 45%, #6a6a6a 0, #3c3c3c 45%, #1e1e1e 100%); }
  .hero-title { position: absolute; left: 0; right: 0; top: 240px; text-align: center;
    font-size: 54px; font-weight: 500; color: var(--white); line-height: 1; }

  .portrait-frame { position: absolute; left: 90px; top: 550px; width: 339px; height: 397px;
    border-right: 1px solid var(--pink); border-bottom: 1px solid var(--pink);
    border-radius: 0 0 62px 0; }
  .portrait { position: absolute; left: 84px; top: 544px; width: 340px; height: 397px;
    border-radius: 59px 0 59px 0;
    background: linear-gradient(150deg, #f2f2f2 0%, #bdbdbd 55%, #8a8a8a 100%); }

  .about { position: absolute; left: 480px; top: 550px; width: 360px; }
  .about h1 { font-size: 35px; font-weight: 400; line-height: 1; }
  .about h1 span { color: var(--pink); }
  .about p { margin-top: 12px; font-size: 9.6px; line-height: 14.8px; color: var(--text-muted); }
  .tagline { position: absolute; left: 478px; top: 699px; font-size: 15.5px; line-height: 24px; }

  .link-row { position: absolute; left: 481px; width: 310px; height: 40px;
    border: 1px solid var(--pink); display: flex; align-items: center; padding: 0 10px 0 14px; }
  .link-row .icon { width: 22px; display: flex; justify-content: center; }
  .link-row .label { margin-left: 14px; font-size: 10.5px; font-weight: 700; color: var(--pink); flex: 1; }
  .link-row .click { width: 50px; height: 20px; border: 1px solid var(--pink); border-radius: 10px;
    font-size: 8px; font-weight: 700; color: var(--pink); display: flex; align-items: center; justify-content: center; }
  .link-row.is-featured { background: linear-gradient(90deg, var(--pink-deep), #f5c4dc); border-color: transparent;
    box-shadow: 0 4px 10px rgba(238,164,200,.35); }
  .link-row.is-featured .label { color: var(--black); line-height: 11px; }
  .link-row.is-featured .label small { display: block; font-size: 8.5px; font-weight: 400; text-decoration: underline; }
  .link-row.is-featured .click { background: var(--black); color: var(--white); border-color: var(--black); }

  .site-footer { position: absolute; left: 0; top: 1055px; width: 919px; height: 145px; background: var(--panel); }
  .footer-nav a { position: absolute; top: 34px; font-size: 10px; font-weight: 500; color: #d8d8d8; text-decoration: none; }
  .copyright { position: absolute; top: 64px; width: 100%; text-align: center; font-size: 9px; color: #d0d0d0; }
  .socials { position: absolute; top: 90px; width: 100%; display: flex; justify-content: center; gap: 6px; }
  .socials span { height: 24px; padding: 0 8px; border-radius: 12px; background: var(--pink);
    color: var(--black); font-size: 8px; font-weight: 600; display: flex; align-items: center; }
</style>
</head>
<body>
<div class="page">
  <nav class="site-nav">
    <a class="is-active" style="left:86px">HOME</a>
    <span class="sep" style="left:154px"></span>
    <a style="left:187px">ABOUT ME</a>
    <span class="sep" style="left:276px"></span>
    <a style="left:306px">MY LINKS</a>
    <div class="brand-mark">WickedMarlo</div>
    <a style="left:533px">MY VIDEOS</a>
    <span class="sep" style="left:625px"></span>
    <a style="left:658px">JOIN NOW</a>
    <span class="sep" style="left:746px"></span>
    <a style="left:777px">CONTACT ME</a>
  </nav>

  <section class="hero" role="img" aria-label="Black and white photo of the model lying on a bed">
    <div class="hero-title">WickedMarlo</div>
  </section>

  <div class="portrait-frame"></div>
  <div class="portrait" role="img" aria-label="Black and white portrait of the model"></div>

  <section class="about">
    <h1>About <span>Me</span></h1>
    <p>Lorem Ipsum is simply dummy text of the printing and typesetting industry. Lorem Ipsum has been the industry's standard dummy text ever since the 1500s, when an unknown printer took a galley of type and scrambled it to make a type specimen book. It has survived not only five centuries, but also the leap into electronic typesetting</p>
  </section>
  <div class="tagline">“Queen of Dirty Talk” is important to work in.<br>HOTWIFE SUPER SLUT</div>

  <a class="link-row" style="top:758px">
    <span class="icon"><svg width="14" height="14"><circle cx="7" cy="7" r="6" fill="var(--pink)"/></svg></span>
    <span class="label">FREE PEEKVAULT</span><span class="click">CLICK</span>
  </a>
  <a class="link-row is-featured" style="top:806px">
    <span class="icon"><svg width="20" height="24" viewBox="0 0 20 24"><path d="M5 11V7a5 5 0 0 1 10 0v4" fill="none" stroke="#000" stroke-width="2.5"/><rect x="1" y="10" width="18" height="13" rx="4" fill="#000"/><circle cx="10" cy="15.5" r="2" fill="var(--pink)"/><rect x="9" y="16" width="2" height="4" fill="var(--pink)"/></svg></span>
    <span class="label">VIP PEEKVAULT<small>www.peekvault.com/wickedmarlovip</small></span><span class="click">CLICK</span>
  </a>
  <a class="link-row" style="top:855px">
    <span class="icon"><svg width="14" height="14"><rect x="1" y="1" width="12" height="12" fill="var(--pink)"/></svg></span>
    <span class="label">CLIPHAUS</span><span class="click">CLICK</span>
  </a>
  <a class="link-row" style="top:903px">
    <span class="icon"><svg width="14" height="14"><circle cx="7" cy="7" r="6" fill="var(--pink)"/></svg></span>
    <span class="label">CASHWIX</span><span class="click">CLICK</span>
  </a>
  <a class="link-row" style="top:950px">
    <span class="icon"><svg width="14" height="14"><circle cx="7" cy="7" r="6" fill="var(--pink)"/></svg></span>
    <span class="label">PICTORA</span><span class="click">CLICK</span>
  </a>

  <footer class="site-footer">
    <nav class="footer-nav">
      <a style="left:237px">HOME</a>
      <a style="left:326px">ABOUT ME</a>
      <a style="left:434px">LINKS</a>
      <a style="left:518px">MY VIDEOS</a>
      <a style="left:623px">CONTACT ME</a>
    </nav>
    <div class="copyright">Copyright © 2020-2021 Wickedmarlo | Privacy | Terms</div>
    <div class="socials"><span>Friendlyn</span><span>Cashwix</span><span>ClipHaus</span><span>Pictora</span></div>
  </footer>
</div>
</body>
</html>
```